Tree Pruning Website

We need a website for a tree Arborist, pruning company called Hollow Ridge Groundcare. We look after all types of trees, knock down trees and prune trees. Our target market is from domestic clients to government clients and everything in between.

We would like to see the use of our main colours which are orange and green

We are not looking forward in seeing a template that we have seen before but a unique template. We have designed 5 templates ourselves and we wish for the design community to take our designs to the next level.

We have also designed a template for things that **we are not** looking for (Version 4)

To make it fair for everyone, we are also not giving out any participation payments as we have had. One winner will take all of the payment!!!

I Have attached a image of the designs and a image of a tree.

We are just looking at the PSD file been developed. We have our own team who can slice the image up into a HTML format.

Target Market(s)

Everyone who needs to cut down a tree

Industry/Entity Type

Government

Requirements
Must have
• Logo on front page
A List of our services
jQuery slider on page
Phone Number on every page

```html
<!DOCTYPE html>
<html lang="en">
<head>
<meta charset="utf-8">
<title>Hollow Ridge Groundcare – Tree Pruning Perth</title>
<link href="https://fonts.googleapis.com/css2?family=Arvo:wght@400;700&family=Open+Sans:ital,wght@0,400;0,600;0,700;1,400&family=Roboto+Condensed:wght@400&family=Arimo:wght@400;700&display=swap" rel="stylesheet">
<style>
:root{
  --orange:#f2560a;
  --orange-dark:#d94a06;
  --orange-deep:#c9470a;
  --green:#5fa300;
  --green-dark:#4a8500;
  --leaf-bg-top:#6c8550;
  --leaf-bg-bottom:#1d4a07;
  --ink:#3a3a3a;
  --muted:#777;
  --panel:#eef0f2;
  --white:#fff;
}
*{box-sizing:border-box;margin:0;padding:0}
html,body{width:924px;height:1200px;overflow:hidden}
body{
  position:relative;
  font-family:'Open Sans',sans-serif;
  color:var(--ink);
  background:
    radial-gradient(circle at 12% 18%, rgba(190,200,150,.35) 0 90px, transparent 190px),
    radial-gradient(circle at 88% 22%, rgba(170,190,130,.35) 0 80px, transparent 200px),
    radial-gradient(circle at 80% 45%, rgba(60,110,20,.5) 0 60px, transparent 180px),
    linear-gradient(180deg,var(--leaf-bg-top) 0%,#4e7432 30%,#2f6012 52%,var(--leaf-bg-bottom) 100%);
}
.abs{position:absolute}

/* header */
.brand{left:239px;top:0;width:139px;height:94px;background:var(--green);display:flex;align-items:center;justify-content:center;gap:7px;padding:0 8px}
.brand-dot{width:14px;height:14px;border-radius:50%;background:var(--white);flex:none}
.brand-name{font-family:'Open Sans',sans-serif;font-weight:700;color:var(--white);font-size:12px;line-height:13px}
.main-nav{left:420px;top:74px;display:flex;height:24px;font-family:'Arimo',sans-serif;font-size:7.5px}
.main-nav a{color:var(--white);text-decoration:none;display:flex;align-items:center;padding:0 7px}
.main-nav a.is-active{background:var(--orange);padding:0 8px}

/* slider */
.slider{left:231px;top:100px;width:462px;height:228px;border:2px solid var(--green);background:radial-gradient(ellipse at 50% 70%,#b08a5a 0 40px,transparent 110px),radial-gradient(ellipse at 30% 20%,#c9d6df 0 50px,transparent 120px),linear-gradient(135deg,#6f8a3a,#b07a3a 45%,#7c9a48 70%,#a9b9c0)}
.slider-arrow{width:24px;height:24px;border-radius:50%;border:2px solid var(--orange);background:rgba(0,0,0,.15);top:208px}
.slider-arrow svg{display:block}
.slider-dots{left:440px;top:312px;display:flex;gap:4px}
.slider-dots span{width:11px;height:11px;border-radius:50%;background:#444;border:2px solid #fff}
.slider-dots span.on{background:var(--orange)}

/* intro band */
.intro{left:231px;top:328px;width:462px;height:60px;background:linear-gradient(180deg,#ff6010,var(--orange-dark))}
.intro-text{left:244px;top:337px;width:292px;font-family:'Arimo',sans-serif;font-size:10.3px;line-height:13.6px;color:#fff7ef}
.intro-text strong{color:#2f5e00;font-weight:700}
.call{left:539px;top:328px;width:154px;height:60px;background:linear-gradient(180deg,#f7650f,var(--orange-deep));box-shadow:-4px 4px 8px rgba(0,0,0,.25)}
.call-icon{left:550px;top:343px;width:29px;height:29px;border-radius:50%;background:#7a2a05;border:2px solid #ffb07a;display:flex;align-items:center;justify-content:center}
.call-number{left:589px;top:346px;font-family:'Roboto Condensed',sans-serif;font-size:17.5px;color:#fff}

/* content sheet */
.sheet{left:231px;top:388px;width:462px;height:616px;background:var(--white)}
.sheet-shadow{left:231px;top:388px;width:462px;height:20px;background:linear-gradient(180deg,rgba(0,0,0,.12),transparent)}
.ribbon{left:193px;top:434px;width:537px;height:36px}
.sector{top:483px;width:104px;text-align:center}
.sector h3{font-family:'Arvo',serif;font-weight:400;font-size:10.5px;color:#333;letter-spacing:.3px;white-space:nowrap}
.sector p{font-size:6.2px;line-height:10px;color:var(--muted);margin-top:9px;height:41px}
.btn{display:inline-block;background:var(--green);color:#fff;font-size:6.5px;font-weight:600;padding:3px 4px;border:1px solid #8ed13a;border-radius:1px;text-decoration:none;white-space:nowrap}
.sector .btn{margin-top:13px}

.section-title{font-family:'Arvo',serif;font-size:10.5px;color:#333;font-weight:400;white-space:nowrap}
.rule{height:4px;background:var(--green)}
.rule::after{content:"";position:absolute;left:0;top:4px;border-left:6px solid var(--green);border-bottom:6px solid transparent}
.rule-wrap{position:absolute}
.hr-top{height:1px;background:#e2e2e2}

.overview{left:235px;top:642px;width:338px;font-size:6.3px;line-height:8.7px;color:#555}
.overview p{margin-bottom:8.6px}
.overview .hl{color:var(--green)}
.why-list{left:583px;top:643px;width:106px;list-style:none;font-size:5.7px;color:var(--green);white-space:nowrap}
.why-list li{height:17.3px;display:flex;align-items:center;gap:4px}
.why-list svg{flex:none}

.projects{top:819px;width:121px;height:112px;background:var(--panel)}
.project-photo{position:absolute;left:0;top:0;width:106px;height:77px;border:2px solid var(--orange)}
.project-photo::after{content:"";position:absolute;left:-2px;top:75px;width:106px;height:4px;background:var(--green)}
.projects h4{position:absolute;left:4px;top:87px;font-family:'Arvo',serif;font-weight:400;font-size:7.3px;color:#333}
.projects small{position:absolute;left:4px;top:98px;font-family:'Arvo',serif;font-size:5.5px;color:#999}
.mini-arrow{width:12px;height:12px;border-radius:50%;border:1px solid #ccc;top:778px}

.tweets{left:582px;top:819px;width:106px;height:112px;background:#f5f6f7;border:1px solid #ddd;padding:8px 8px;font-size:4.8px;line-height:6.6px;color:#444}
.tweets p{margin-bottom:6.6px}
.tweets .handle{color:var(--green-dark)}
.tweet-dot{left:588px;top:776px;width:15px;height:15px;border-radius:50%;background:#555}

/* testimonial */
.quote-band{left:231px;top:954px;width:462px;height:50px;background:var(--panel)}
.quote-text{left:288px;top:970px;width:286px;font-style:italic;font-size:6.2px;line-height:9px;color:#444}
.quote-toggle{left:457px;width:10px;height:9px;background:var(--green)}
.quote-author{left:618px;top:977px;font-size:5.8px;color:#333;white-space:nowrap}
.quote-author b{font-weight:700}

/* footer */
.footer{left:231px;top:1004px;width:462px;height:174px;background:linear-gradient(180deg,#ff5400 0%,var(--orange-dark) 70%,#c8500f 100%)}
.footer-col{top:1029px}
.footer-col h5{font-family:'Arvo',serif;font-weight:400;font-size:7.5px;color:#3a1500;margin-bottom:12px}
.footer-col p{font-size:5.3px;line-height:8.6px;color:#fff}
.footer-col p+p{margin-top:8.6px}
.thumb{width:27px;height:27px;border:1px solid #fff}
.map{left:585px;top:1053px;width:102px;height:53px;border:1px solid #ddd;background:linear-gradient(135deg,#e7e3d8,#d8dfcf 50%,#e9e6dd)}
.contact-line{left:587px;font-size:5.2px;color:#fff;display:flex;align-items:center;gap:6px}
.copyright{left:237px;top:1184px;font-size:5px;color:#cfe0b8}
.social{top:1184px;width:9px;height:9px;background:#3b5a20;border-radius:1px}
</style>
</head>
<body>

<header>
  <div class="abs brand" aria-label="Hollow Ridge Groundcare">
    <span class="brand-dot"></span>
    <span class="brand-name">Hollow Ridge<br>Groundcare</span>
  </div>
  <nav class="abs main-nav">
    <a class="is-active" href="#">Home</a>
    <a href="#">About Us</a>
    <a href="#">Our Services</a>
    <a href="#">Get A quote</a>
    <a href="#">Our Work</a>
    <a href="#">Contact Us</a>
  </nav>
</header>

<section class="hero">
  <div class="abs slider" role="img" aria-label="Looking up the trunk of a large spreading tree into its canopy"></div>
  <div class="abs slider-arrow" style="left:202px">
    <svg width="20" height="20" viewBox="0 0 20 20"><path d="M15 10H5M9 6l-4 4 4 4" stroke="#fff" stroke-width="2" fill="none"/></svg>
  </div>
  <div class="abs slider-arrow" style="left:699px">
    <svg width="20" height="20" viewBox="0 0 20 20"><path d="M5 10h10M11 6l4 4-4 4" stroke="#fff" stroke-width="2" fill="none"/></svg>
  </div>
  <div class="abs slider-dots"><span class="on"></span><span></span><span></span></div>

  <div class="abs intro"></div>
  <p class="abs intro-text">Hollow Ridge is the leading tree pruning services located Perth. Our motto is when you call, we <strong>guarantee</strong> to turn up and <strong>provide care</strong> to our customers.</p>
  <div class="abs call"></div>
  <div class="abs call-icon">
    <svg width="14" height="14" viewBox="0 0 24 24"><path fill="#fff" d="M6.6 10.8a15 15 0 0 0 6.6 6.6l2.2-2.2c.3-.3.7-.4 1-.2 1.1.4 2.3.6 3.6.6.6 0 1 .4 1 1V20c0 .6-.4 1-1 1A17 17 0 0 1 3 4c0-.6.4-1 1-1h3.5c.6 0 1 .4 1 1 0 1.3.2 2.5.6 3.6.1.3 0 .7-.2 1z"/></svg>
  </div>
  <div class="abs call-number">08 5550 0142</div>
</section>

<main>
  <div class="abs sheet"></div>
  <div class="abs sheet-shadow"></div>

  <svg class="abs ribbon" viewBox="0 0 537 36" aria-hidden="true">
    <polygon points="0,13 36,13 36,36 12,36 20,24" fill="#c9420a"/>
    <polygon points="537,13 501,13 501,36 525,36 517,24" fill="#c9420a"/>
    <polygon points="36,36 45,28 36,28" fill="#7a2400"/>
    <polygon points="501,36 492,28 501,28" fill="#7a2400"/>
    <rect x="45" y="0" width="447" height="28" fill="#f2560a"/>
    <g fill="#7a2a05" stroke="#ffb07a" stroke-width="2">
      <circle cx="97" cy="14" r="14"/><circle cx="211" cy="14" r="14"/><circle cx="327" cy="14" r="14"/><circle cx="443" cy="14" r="14"/>
    </g>
    <g fill="#fff">
      <rect x="93" y="9" width="8" height="11" rx="1"/><rect x="95" y="6" width="4" height="3"/>
      <path d="M203 10h7v9h-7zM212 10h7v9h-7z"/>
      <circle cx="327" cy="10" r="3.5"/><path d="M320 21c1-5 4-6 7-6s6 1 7 6z"/>
      <path d="M437 20c0-7 5-12 12-12 0 7-5 12-12 12z"/>
    </g>
  </svg>

  <section class="sector abs" style="left:238px">
    <h3>DOMESTIC</h3>
    <p>At vero eos et accusam et justo duo dolores et ea rebum. Stet clita kasd gubergren, no sea takimata sanctus est Lorem ipsum dolor sit amet.</p>
    <a class="btn" href="#">Learn more</a>
  </section>
  <section class="sector abs" style="left:352px">
    <h3>COMMERCIAL</h3>
    <p>Ut wisi enim ad minim veniam, quis nostrud exerci tation ullamcorper suscipit lobortis nisl ut aliquip ex ea commodo consequat.</p>
    <a class="btn" href="#">Learn more</a>
  </section>
  <section class="sector abs" style="left:468px">
    <h3>GOVERMENT</h3>
    <p>Nam liber tempor cum soluta nobis eleifend option congue nihil imperdiet doming id quod mazim placerat facer possim assum.</p>
    <a class="btn" href="#">Learn more</a>
  </section>
  <section class="sector abs" style="left:583px">
    <h3>NON PROFIT</h3>
    <p>Lorem ipsum dolor sit amet, consetetur sadipscing elitr, sed diam nonumy eirmod tempor invidunt ut labore et dolore.</p>
    <a class="btn" href="#">Learn more</a>
  </section>

  <div class="abs hr-top" style="left:235px;top:597px;width:338px"></div>
  <div class="abs hr-top" style="left:583px;top:597px;width:106px"></div>

  <h2 class="abs section-title" style="left:235px;top:603px">Company Overview</h2>
  <div class="rule-wrap" style="left:235px;top:621px;width:338px"><div class="rule"></div></div>
  <div class="abs overview">
    <p><span class="hl">Duis autem vel eum iriure</span> dolor in hendrerit in vulputate velit esse molestie consequat, vel illum dolore eu feugiat nulla facilisis at vero eros et accumsan et iusto odio dignissim qui blandit praesent luptatum zzril delenit augue duis dolore te feugait nulla facilisi. Lorem ipsum dolor sit amet, consectetuer adipiscing elit, sed diam nonummy nibh euismod tincidunt ut laoreet dolore magna aliquam erat volutpat.</p>
    <p>Ut wisi enim ad minim veniam, quis nostrud exerci tation ullamcorper suscipit lobortis nisl ut <span class="hl">aliquip ex ea commodo consequat.</span> Duis autem vel eum iriure dolor in hendrerit in vulputate velit esse molestie consequat, vel illum dolore eu feugiat nulla facilisis at vero eros et accumsan et iusto odio dignissim qui blandit praesent luptatum zzril delenit augue duis dolore te feugait nulla facilisi. Nam liber tempor cum soluta nobis eleifend option congue nihil imperdiet doming id quod mazim placerat facer possim assum. Lorem ipsum dolor sit amet.</p>
    <p class="hl">Ut laoreet dolore magna aliquam erat volutpat. Ut wisi enim ad minim veniam, quis nostrud exerci tation ullamcorper suscipit lobortis nisl ut aliquip ex ea commodo consequat.</p>
  </div>

  <h2 class="abs section-title" style="left:585px;top:603px;font-size:10px">Why Hollow Ridge?</h2>
  <div class="rule-wrap" style="left:583px;top:621px;width:106px"><div class="rule"></div></div>
  <ul class="abs why-list">
    <li><svg width="8" height="5" viewBox="0 0 8 5"><path d="M0 2.5h7M5 .5l2 2-2 2" stroke="#5fa300" fill="none"/></svg>Doloor in hendrerit in vulputate</li>
    <li><svg width="8" height="5" viewBox="0 0 8 5"><path d="M0 2.5h7M5 .5l2 2-2 2" stroke="#5fa300" fill="none"/></svg>Velit esse molestie consequat</li>
    <li><svg width="8" height="5" viewBox="0 0 8 5"><path d="M0 2.5h7M5 .5l2 2-2 2" stroke="#5fa300" fill="none"/></svg>Vel illum dolore eu feugiat</li>
    <li><svg width="8" height="5" viewBox="0 0 8 5"><path d="M0 2.5h7M5 .5l2 2-2 2" stroke="#5fa300" fill="none"/></svg>Nulla facilisis at vero eros et</li>
    <li><svg width="8" height="5" viewBox="0 0 8 5"><path d="M0 2.5h7M5 .5l2 2-2 2" stroke="#5fa300" fill="none"/></svg>Accumsan et iusto odio dignissim</li>
    <li><svg width="8" height="5" viewBox="0 0 8 5"><path d="M0 2.5h7M5 .5l2 2-2 2" stroke="#5fa300" fill="none"/></svg>Qui blandit praesent luptatum zzr.</li>
  </ul>

  <div class="abs hr-top" style="left:235px;top:771px;width:338px"></div>
  <div class="abs hr-top" style="left:583px;top:771px;width:106px"></div>
  <h2 class="abs section-title" style="left:235px;top:777px">Our Services</h2>
  <div class="abs mini-arrow" style="left:545px"></div>
  <div class="abs mini-arrow" style="left:559px"></div>
  <div class="rule-wrap" style="left:235px;top:795px;width:338px"><div class="rule"></div></div>

  <article class="abs projects" style="left:236px">
    <div class="project-photo" role="img" aria-label="Pale eucalyptus trunks against the sky" style="background:linear-gradient(135deg,#dfe6ea,#b9c3c8 50%,#8a8f7a)"></div>
    <h4>Observation 1</h4><small>Locations</small>
  </article>
  <article class="abs projects" style="left:352px">
    <div class="project-photo" role="img" aria-label="Leafy canopy seen from below" style="background:radial-gradient(circle at 50% 50%,#2c3a1c,#4f8a2a 60%,#a9c47a)"></div>
    <h4>Observation 1</h4><small>Locations</small>
  </article>
  <article class="abs projects" style="left:467px">
    <div class="project-photo" role="img" aria-label="Sunlit forest path between tall trees" style="background:radial-gradient(ellipse at 55% 40%,#e9e2a6 0 10px,#7d9a3a 35px,#2f4a14 70px)"></div>
    <h4>Observation 1</h4><small>Locations</small>
  </article>

  <div class="abs tweet-dot"></div>
  <h2 class="abs section-title" style="left:614px;top:777px">Twitter</h2>
  <div class="rule-wrap" style="left:583px;top:795px;width:106px"><div class="rule"></div></div>
  <div class="abs tweets">
    <p><span class="handle">@hollowridgegc</span> Stet clita kasd gubergren, no sea takimata sanctus est Lorem ipsum....by <span class="handle">hollowridgegc</span><br>about 2 hour ago</p>
    <p><span class="handle">@hollowridgegc</span> Stet clita kasd gubergren, no sea takimata sanctus est Lorem ipsum....by <span class="handle">hollowridgegc</span><br>about 2 hour ago</p>
    <p><span class="handle">@hollowridgegc</span> Stet clita kasd gubergren, no sea takimata sanctus est Lorem ipsum....by <span class="handle">hollowridgegc</span><br>about 2 hour ago</p>
  </div>

  <section class="testimonial">
    <div class="abs quote-band"></div>
    <svg class="abs" style="left:246px;top:968px" width="28" height="22" viewBox="0 0 28 22" aria-hidden="true">
      <path d="M2 2h16v10H8l-4 4v-4H2z" fill="#333"/><path d="M20 6h6v10h-2v4l-4-4h-8v-2h8z" fill="#333"/>
    </svg>
    <div class="abs quote-toggle" style="top:954px"></div>
    <div class="abs quote-toggle" style="top:995px"></div>
    <p class="abs quote-text">" Duis autem vel eum iriure dolor in hendrerit in feugiat nulla facilisis at vero eros et accumsan vulputate velit esse molestie consequat, vel illum dolore eu pasto. "</p>
    <div class="abs" style="left:587px;top:962px;width:1px;height:34px;background:#ccc"></div>
    <svg class="abs" style="left:597px;top:975px" width="12" height="12" viewBox="0 0 12 12" aria-hidden="true"><circle cx="6" cy="3.5" r="3" fill="#444"/><path d="M0 12c0-4 3-5 6-5s6 1 6 5z" fill="#444"/></svg>
    <p class="abs quote-author"><b>Mara Ellison</b> - Goverment -</p>
  </section>
</main>

<footer>
  <div class="abs footer"></div>
  <svg class="abs" style="left:240px;top:1003px" width="40" height="16" viewBox="0 0 40 16" aria-hidden="true"><polygon points="0,0 34,0 0,16" fill="#eef0f2"/></svg>

  <div class="abs footer-col" style="left:236px;width:105px">
    <h5>ABOUT US</h5>
    <p>Lorem ipsum dolor sit amet, consetetur sadipscing elitr, sed diam nonumy eirmod tempor invidunt ut labore et dolore magna aliquyam erat, sed diam voluptua. At vero eos et accusam et justo duo dolores et ea rebum. Stet clita kasd gubergren, no sea takimata sanctus est Lorem ipsum dolor sit amet</p>
  </div>
  <div class="abs footer-col" style="left:351px;width:100px">
    <h5>LATEST NEWS</h5>
    <p>Lorem ipsum dolor sit amet, consetetur sadipscing elitr, sed diam.</p>
    <p>Nonumy eirmod tempor invidunt ut.</p>
    <p>Labore et dolore magna aliquyam erat, sed diam voluptua.</p>
    <p>At vero eos et accusam et justo duo dolores et ea rebum.</p>
  </div>
  <div class="abs footer-col" style="left:467px">
    <h5>GALLERY</h5>
  </div>
  <div class="abs thumb" style="left:467px;top:1053px;background:linear-gradient(#fff,#cfe7f2 60%,#3c8a1e)" role="img" aria-label="Water drop on a seedling"></div>
  <div class="abs thumb" style="left:507px;top:1053px;background:linear-gradient(135deg,#f4e7da,#c89a78)" role="img" aria-label="Client in a garden"></div>
  <div class="abs thumb" style="left:546px;top:1053px;background:linear-gradient(#7ab6d0,#3f7e2a)" role="img" aria-label="Green landscape under sky"></div>
  <div class="abs thumb" style="left:467px;top:1091px;background:linear-gradient(#f2f7e6,#6fb42a)" role="img" aria-label="Fresh grass blades"></div>
  <div class="abs thumb" style="left:507px;top:1091px;background:linear-gradient(135deg,#2f5a12,#8fc64a)" role="img" aria-label="Leaves in sunlight"></div>
  <div class="abs thumb" style="left:546px;top:1091px;background:linear-gradient(135deg,#cfe0a8,#e6d6c8)" role="img" aria-label="Person outdoors among greenery"></div>
  <a class="abs btn" href="#" style="left:527px;top:1132px;width:46px;height:16px;font-size:7px;font-weight:400;padding:3px 0;text-align:center">more gallery</a>

  <div class="abs footer-col" style="left:585px">
    <h5>GET IN TOUCH</h5>
  </div>
  <div class="abs map" role="img" aria-label="Street map showing the yard location"></div>
  <svg class="abs" style="left:636px;top:1070px" width="10" height="14" viewBox="0 0 10 14" aria-hidden="true"><path d="M5 0a5 5 0 0 1 5 5c0 4-5 9-5 9S0 9 0 5a5 5 0 0 1 5-5z" fill="#d33"/><circle cx="5" cy="5" r="2" fill="#fff"/></svg>
  <p class="abs contact-line" style="top:1117px;display:block;line-height:8.6px">14 Larchmont Lane<br>BRAMBLEFORD, WA 6999</p>
  <p class="abs contact-line" style="top:1141px"><svg width="7" height="6" viewBox="0 0 24 24"><path fill="#fff" d="M6.6 10.8a15 15 0 0 0 6.6 6.6l2.2-2.2c.3-.3.7-.4 1-.2 1.1.4 2.3.6 3.6.6.6 0 1 .4 1 1V20c0 .6-.4 1-1 1A17 17 0 0 1 3 4c0-.6.4-1 1-1h3.5c.6 0 1 .4 1 1 0 1.3.2 2.5.6 3.6.1.3 0 .7-.2 1z"/></svg>08 5550 0178</p>
  <p class="abs contact-line" style="top:1152px;color:#ffd7bd"><svg width="7" height="6" viewBox="0 0 7 6"><rect x=".5" y=".5" width="6" height="5" fill="none" stroke="#ffd7bd"/></svg>08 5550 0178</p>
  <p class="abs contact-line" style="top:1163px"><svg width="7" height="6" viewBox="0 0 7 6"><rect x=".5" y=".5" width="6" height="5" fill="none" stroke="#fff"/><path d="M.5.5l3 3 3-3" stroke="#fff" fill="none"/></svg>hello@hollowridge.example</p>

  <p class="abs copyright">© Copyright 2013 Hollow Ridge Groundcare.</p>
  <span class="abs social" style="left:647px"></span>
  <span class="abs social" style="left:663px"></span>
  <span class="abs social" style="left:679px"></span>
</footer>

</body>
</html>
```